Tarvin Building Solutions (building inspections and small construction
Tarvin Building Solutions
Professional
Gareth Lowell
42 Pellam St Dunmore Vale
0427 3 TARVI (82784)
gary@tarvinbuildingsolutions.com.au
www.tarvinbuildingsolutions.com.au
Builders Licence:918037F
at the base of the business card it should read: In association with J&T Corbel and Associates see J & T logo attached. I also want to show member of WQD ( See wqd logo attached). Also dwellguard accredited (see attached logo)
New Construction Q&A
Mould and Asbestos ID
Pre-Purchase
Pool Safety
Defect & Warranty
Decks
Pergolas
Bathroom Renovations
Home Renovations
This is my TBS Logo
another copy of logo
This logo is for in association with J & T Corbel
Member of WQD logo. Please put on back of card
Accredited with Dwellguard. Please put on back of card

```html
<!DOCTYPE html>
<html lang="en">
<head>
<meta charset="utf-8">
<title>Tarvin Building Solutions — Stationery</title>
<link rel="stylesheet" href="https://fonts.googleapis.com/css2?family=Montserrat:wght@400;600;700&family=Open+Sans:wght@400;600&display=swap">
<style>
:root{
  --bg:#2b2b2b;
  --paper:#ffffff;
  --ink:#111214;
  --blue:#3a8ee6;
  --blue-light:#8cc4ff;
  --grey:#6d7178;
  --line:#d5d8dc;
  --silver:#c9ccd1;
}
*{box-sizing:border-box;margin:0;padding:0}
html,body{width:1200px;height:845px;overflow:hidden;background:var(--bg)}
body{position:relative;font-family:"Open Sans",Arial,sans-serif;color:var(--ink)}
.sheet{position:absolute;background:var(--paper);overflow:hidden}
.band{position:absolute;left:0;top:0;width:100%;display:block}
.brand{position:absolute;display:flex;align-items:center;gap:6px;font-family:"Montserrat",Arial,sans-serif;font-weight:700;color:var(--blue);letter-spacing:.02em;white-space:nowrap}
.brand-dot{width:9px;height:9px;border-radius:50%;background:var(--blue);flex:none}

/* letterhead */
.letterhead{left:40px;top:40px;width:330px;height:467px}
.letterhead .brand{left:20px;top:16px;font-size:11px}
.letterhead-footer{position:absolute;left:0;bottom:0;width:100%;height:34px;background:var(--ink);border-top:3px solid var(--blue);color:#fff;font-size:6.5px;display:flex;align-items:center;justify-content:center;gap:10px}

/* invoice */
.invoice{left:400px;top:40px;width:330px;height:467px}
.invoice .brand{left:20px;top:16px;font-size:11px}
.invoice-meta{position:absolute;right:18px;top:76px;font-size:7px;text-align:right;line-height:1.6;color:var(--grey)}
.invoice-title{font-family:"Montserrat",Arial,sans-serif;font-weight:700;font-size:14px;color:var(--ink)}
.party{position:absolute;top:118px;width:140px;height:56px;border:1px solid var(--line);font-size:7px;padding:4px 6px}
.party b{font-family:"Montserrat",Arial,sans-serif;color:var(--ink);font-size:7.5px}
.party.bill{left:18px}.party.ship{left:172px}
.items{position:absolute;left:18px;top:186px;width:294px;border-collapse:collapse;font-size:7px}
.items th{background:var(--ink);color:#fff;font-weight:600;text-align:left;padding:4px 5px;border-bottom:2px solid var(--blue)}
.items td{height:15px;border-bottom:1px solid var(--line);border-left:1px solid var(--line)}
.items td:last-child{border-right:1px solid var(--line)}
.invoice-total{position:absolute;right:18px;top:415px;font-size:8px;font-weight:600;border:1px solid var(--ink);padding:3px 10px}
.invoice-note{position:absolute;left:18px;top:418px;font-size:7px;color:var(--grey)}
.invoice-footer{position:absolute;left:0;bottom:0;width:100%;height:14px;background:var(--ink);border-top:2px solid var(--blue)}

/* envelopes */
.envelope-front{left:760px;top:40px;width:400px;height:200px}
.envelope-front .brand{left:18px;top:14px;font-size:11px}
.return-address{position:absolute;left:18px;top:62px;font-size:7px;color:var(--grey);line-height:1.5}
.envelope-back{left:760px;top:270px;width:400px;height:237px}
.envelope-back .brand{left:50%;transform:translateX(-50%);top:40px;font-size:12px}

/* business cards */
.card{top:560px;width:380px;height:217px}
.card-front{left:110px}
.card-front .brand{left:22px;top:24px;font-size:14px}
.card-tagline{position:absolute;left:38px;top:46px;font-size:8px;letter-spacing:.3em;color:var(--grey);text-transform:uppercase}
.card-person{position:absolute;right:22px;top:150px;text-align:right;color:#fff}
.card-name{font-family:"Montserrat",Arial,sans-serif;font-weight:600;font-size:15px}
.card-role{font-size:8px;color:var(--blue-light);letter-spacing:.15em;text-transform:uppercase}
.card-back{left:710px;background:var(--ink);color:#fff}
.card-back .brand{left:18px;top:14px;font-size:11px;color:var(--blue-light)}
.card-back .brand-dot{background:var(--blue-light)}
.contact-list{position:absolute;left:18px;top:42px;list-style:none;font-size:7.4px;line-height:1.75}
.contact-list li{display:flex;align-items:center;gap:5px}
.contact-list svg{width:8px;height:8px;flex:none}
.services{position:absolute;right:16px;top:14px;list-style:none;font-size:7.2px;line-height:1.65;text-align:right;color:var(--silver)}
.card-base{position:absolute;left:0;bottom:0;width:100%;height:46px;background:#1b1c1f;border-top:2px solid var(--blue);display:flex;align-items:center;padding:0 14px;gap:10px}
.partner-badge{width:40px;height:26px;border-radius:3px;background:var(--silver);flex:none}
.partner-badge.round{width:28px;height:28px;border-radius:50%;background:var(--blue)}
.association{font-size:7.4px;line-height:1.3;color:#fff;flex:1}
.association b{font-family:"Montserrat",Arial,sans-serif;font-weight:600;color:var(--blue-light)}
</style>
</head>
<body>

<!-- Letterhead -->
<section class="sheet letterhead" aria-label="Letterhead">
  <svg class="band" viewBox="0 0 330 70" width="330" height="70" preserveAspectRatio="none">
    <polygon points="0,0 330,0 330,40 210,58 0,46" fill="#111214"/>
    <polyline points="0,46 210,58 330,40" fill="none" stroke="#3a8ee6" stroke-width="3"/>
  </svg>
  <div class="brand"><span class="brand-dot"></span>Tarvin Building Solutions</div>
  <footer class="letterhead-footer">
    <span>42 Pellam St Dunmore Vale</span>
    <span>0427 3 TARVI (82784)</span>
    <span>www.tarvinbuildingsolutions.com.au</span>
  </footer>
</section>

<!-- Invoice -->
<section class="sheet invoice" aria-label="Invoice">
  <svg class="band" viewBox="0 0 330 70" width="330" height="70" preserveAspectRatio="none">
    <polygon points="0,0 330,0 330,40 210,58 0,46" fill="#111214"/>
    <polyline points="0,46 210,58 330,40" fill="none" stroke="#3a8ee6" stroke-width="3"/>
  </svg>
  <div class="brand"><span class="brand-dot"></span>Tarvin Building Solutions</div>
  <div class="invoice-meta">
    <div class="invoice-title">TAX INVOICE</div>
    <div>Invoice No. ______</div>
    <div>Date ______</div>
  </div>
  <div class="party bill"><b>BILL TO:</b></div>
  <div class="party ship"><b>SHIP TO:</b></div>
  <table class="items">
    <thead><tr><th>Description</th><th>Qty</th><th>Rate</th><th>Amount</th></tr></thead>
    <tbody>
      <tr><td style="width:55%"></td><td></td><td></td><td></td></tr>
      <tr><td></td><td></td><td></td><td></td></tr>
      <tr><td></td><td></td><td></td><td></td></tr>
      <tr><td></td><td></td><td></td><td></td></tr>
      <tr><td></td><td></td><td></td><td></td></tr>
      <tr><td></td><td></td><td></td><td></td></tr>
      <tr><td></td><td></td><td></td><td></td></tr>
      <tr><td></td><td></td><td></td><td></td></tr>
      <tr><td></td><td></td><td></td><td></td></tr>
      <tr><td></td><td></td><td></td><td></td></tr>
      <tr><td></td><td></td><td></td><td></td></tr>
      <tr><td></td><td></td><td></td><td></td></tr>
    </tbody>
  </table>
  <p class="invoice-note">Thank you for your business</p>
  <div class="invoice-total">Total</div>
  <div class="invoice-footer"></div>
</section>

<!-- Envelope front -->
<section class="sheet envelope-front" aria-label="Envelope front">
  <svg class="band" viewBox="0 0 400 200" width="400" height="200" preserveAspectRatio="none">
    <polygon points="0,0 400,0 400,18 150,48 0,56" fill="#111214"/>
    <polyline points="0,56 150,48 400,18" fill="none" stroke="#3a8ee6" stroke-width="3"/>
  </svg>
  <div class="brand"><span class="brand-dot"></span>Tarvin Building Solutions</div>
  <address class="return-address">42 Pellam St Dunmore Vale<br>www.tarvinbuildingsolutions.com.au</address>
</section>

<!-- Envelope back -->
<section class="sheet envelope-back" aria-label="Envelope back">
  <svg class="band" viewBox="0 0 400 237" width="400" height="237" preserveAspectRatio="none">
    <path d="M0,0 H400 V40 C330,120 70,120 0,40 Z" fill="#111214"/>
    <path d="M0,40 C70,120 330,120 400,40" fill="none" stroke="#3a8ee6" stroke-width="3"/>
  </svg>
  <div class="brand"><span class="brand-dot"></span>Tarvin Building Solutions</div>
</section>

<!-- Business card front -->
<section class="sheet card card-front" aria-label="Business card front">
  <svg class="band" viewBox="0 0 380 217" width="380" height="217" preserveAspectRatio="none">
    <polygon points="0,120 380,100 380,217 0,217" fill="#111214"/>
    <polyline points="0,120 380,100" fill="none" stroke="#3a8ee6" stroke-width="4"/>
  </svg>
  <div class="brand"><span class="brand-dot"></span>Tarvin Building Solutions</div>
  <div class="card-tagline">Professional</div>
  <div class="card-person">
    <div class="card-name">Gareth Lowell</div>
    <div class="card-role">Builder &amp; Inspector</div>
  </div>
</section>

<!-- Business card back -->
<section class="sheet card card-back" aria-label="Business card back">
  <div class="brand"><span class="brand-dot"></span>Tarvin Building Solutions</div>
  <ul class="contact-list">
    <li><svg viewBox="0 0 10 10"><path d="M5 0C3 0 1.5 1.5 1.5 3.5 1.5 6 5 10 5 10s3.5-4 3.5-6.5C8.5 1.5 7 0 5 0z" fill="#8cc4ff"/></svg>42 Pellam St Dunmore Vale</li>
    <li><svg viewBox="0 0 10 10"><path d="M2 0h2l1 3-1.5 1a6 6 0 0 0 2.5 2.5L7 5l3 1v2c0 1-1 2-2 2A8 8 0 0 1 0 2c0-1 1-2 2-2z" fill="#8cc4ff"/></svg>0427 3 TARVI (82784)</li>
    <li><svg viewBox="0 0 10 10"><rect x="0" y="2" width="10" height="6" fill="none" stroke="#8cc4ff"/><path d="M0 2l5 3.5L10 2" fill="none" stroke="#8cc4ff"/></svg>gary@tarvinbuildingsolutions.com.au</li>
    <li><svg viewBox="0 0 10 10"><circle cx="5" cy="5" r="4.5" fill="none" stroke="#8cc4ff"/><path d="M0.5 5h9M5 0.5c-2 2.5-2 6.5 0 9M5 0.5c2 2.5 2 6.5 0 9" fill="none" stroke="#8cc4ff" stroke-width=".7"/></svg>www.tarvinbuildingsolutions.com.au</li>
    <li>Builders Licence: 918037F</li>
  </ul>
  <ul class="services">
    <li>New Construction Q&amp;A</li>
    <li>Mould and Asbestos ID</li>
    <li>Pre-Purchase</li>
    <li>Pool Safety</li>
    <li>Defect &amp; Warranty</li>
    <li>Decks</li>
    <li>Pergolas</li>
    <li>Bathroom Renovations</li>
    <li>Home Renovations</li>
  </ul>
  <div class="card-base">
    <p class="association">In association with<br><b>J&amp;T Corbel and Associates</b></p>
    <span class="partner-badge" role="img" aria-label="Member of WQD badge"></span>
    <span class="partner-badge round" role="img" aria-label="Dwellguard accredited badge"></span>
  </div>
</section>

</body>
</html>
```